Velmarone Website Redesign

We need a redesign of the company website.

We're a company, based in the UK, called Velmarone. We develop software for the Healthcare Industry, used by medical professionals throughout the UK on a daily basis.

We have a suite of tools that form the Velmarone Platform, and all are web-based.

We want to communicate that our software is not only innovative but is the best available, easy to use, and provides exceptional quality and RoI.

Additionally, we want our existing customers to be able to see what else we can offer them.

A site map is attached.
Updates

Hi Everyone,

As we approach the deadline for submissions, we’ve shortlisted threedesigns that we felt were the best of the submissions and have asked thedesigners to make some additional changes and produce some content pages so wecan see what’s beneath the Home page in the rest of the site.

Thank you all for your submissions – there was an awful lot ofdisagreement among everyone here over which designs we thought were best andsome of those that haven’t made it into the final three were very well liked.

Those in the final three have been messaged individually and have theirdesigns as the only non-eliminated ones showing. We would ask at this stagethat anyone not in the final three please do no further work or submitadditional designs as we are approaching the deadline and will not be able toprovide sufficient feedback to allow any changes in a short space of time.

Kind regards,
The Velmarone Team

Target Market(s)

Nurses and medical professionals in western-speaking countries, most notably in the UK.

Predominantly, we expect it will be senior medical staff that will be viewing (and using) our website - some will be existing customers and some will be new or potential customers.

Industry/Entity Type

Medical

Requirements
Must have
• Area to showcase and provide information about products.
• Company information - who we are and why you should choose us.
• News and events - blog, archive newsletters, publications, etc.
• Support section for existing customers - FAQ, Forum, Manuals.
• Contact page.
• We also feel that we'd like to have our telephone number and primary email address visible at all times, with an immediate ability for users to request a demonstration.
Nice to have
• A "My Velmarone" area would be nice at some point, though that's something for further down the line.

```html
<!DOCTYPE html>
<html lang="en">
<head>
<meta charset="utf-8">
<title>VelmaroneHealth – Home</title>
<link rel="stylesheet" href="https://fonts.googleapis.com/css2?family=Source+Sans+3:wght@400;600;700&family=Open+Sans:wght@400;700&display=swap">
<style>
:root{
  --blue:#1a7fd6;
  --blue-deep:#0f5fae;
  --blue-dark:#0b4e95;
  --blue-link:#0b63c4;
  --grey-text:#6d6d6d;
  --grey-mid:#8b8b8b;
  --grey-line:#d7e3ef;
  --ink:#222;
  --page:#ffffff;
}
*{box-sizing:border-box;margin:0;padding:0}
html,body{width:1200px;height:1068px;overflow:hidden;background:var(--page)}
body{position:relative;font-family:"Open Sans",Tahoma,sans-serif;color:var(--grey-text);
  background:linear-gradient(#eeeeee 0,#fafafa 90px,#fff 150px)}
a{text-decoration:none;color:var(--blue-link)}

.brand{position:absolute;left:90px;top:58px}
.brand-name{font-family:"Source Sans 3",sans-serif;font-weight:700;font-size:36px;color:var(--blue);letter-spacing:-.3px;line-height:1}
.brand-tagline{margin-top:8px;padding-top:6px;border-top:2px solid #c9c9c9;font-family:"Source Sans 3",sans-serif;font-weight:700;font-size:16px;color:var(--grey-mid)}

.main-nav{position:absolute;left:480px;top:76px;width:634px;height:28px;border-bottom:1px solid var(--grey-line);
  display:flex;justify-content:space-between;font-family:"Source Sans 3",sans-serif;font-size:15.5px}
.main-nav a{color:var(--grey-mid);padding:0 2px}
.main-nav a.is-current{color:var(--blue);border-bottom:2px solid var(--blue);height:28px}
.main-nav .amp{color:#c4c4c4}

.hero{position:absolute;left:60px;top:156px;width:1080px;height:223px;
  background:linear-gradient(100deg,#125ea9 0%,#1f78c8 40%,#2d85d0 60%,#156bbb 100%);
  border-bottom:7px solid #0c4f93;border-radius:3px 3px 0 0;overflow:hidden}
.hero-title{position:absolute;left:31px;top:38px;font-family:"Source Sans 3",sans-serif;font-size:29px;color:#fff}
.hero-lead{position:absolute;left:32px;top:92px;font-family:"Source Sans 3",sans-serif;font-size:21px;line-height:27px;color:#e7f1fb}
.hero-photo{position:absolute;left:560px;top:0;width:520px;height:216px;
  background:radial-gradient(ellipse at 35% 55%,#c6dcef 0%,#8fb7dd 40%,rgba(40,128,206,0) 75%)}

.sidebar{position:absolute;left:60px;top:379px;width:324px;height:543px;
  background:linear-gradient(90deg,#fff 0,#fff 85%,#ececec 100%)}
.sidebar-title{position:absolute;left:27px;top:40px;font-family:"Source Sans 3",sans-serif;font-size:22px;color:var(--blue)}
.post{position:absolute;left:27px;width:270px}
.post-title{font-size:13px;font-weight:700;color:var(--blue-link);margin-bottom:6px}
.post-text{font-size:11.5px;line-height:15.5px;color:#555}
.post-more{display:block;text-align:right;font-size:12px;margin-top:1px}

.showcase{position:absolute;left:408px;top:420px;width:709px;height:190px;
  background:linear-gradient(#fff 0,#fff 40px,#f3f5f7 100%)}
.showcase-boxes{position:absolute;left:40px;top:10px;width:600px;height:160px;
  background:linear-gradient(90deg,#ece4f3 0,#d7efe9 18%,#eef3f6 40%,#eef3f6 60%,#dbefe7 82%,#f3e4f0 100%)}

.tagline{position:absolute;left:431px;top:620px;font-family:"Source Sans 3",sans-serif;font-size:29px;color:var(--blue)}
.tagline b{font-weight:600}
.intro{position:absolute;left:431px;top:694px;width:458px;font-size:12.5px;line-height:19.5px;font-weight:700;color:var(--ink)}
.body-copy{position:absolute;left:431px;top:772px;width:458px;font-size:11.5px;line-height:19.5px;color:#777;text-align:justify}
.quick-links{position:absolute;right:83px;top:782px;text-align:right;list-style:none;font-size:13px;font-weight:700;line-height:19.5px}
.quick-links a{color:var(--blue-link)}
.quick-links svg{margin-left:7px;vertical-align:-1px}

.action-bar{position:absolute;left:60px;top:922px;width:1080px;height:61px;background:var(--blue-deep);overflow:hidden}
.my-area{position:absolute;left:0;top:0;width:324px;height:61px;background:linear-gradient(90deg,#2b8ae0,#1a76cc)}
.my-area-name{position:absolute;left:29px;top:17px;font-family:"Source Sans 3",sans-serif;font-size:22px;color:#fff}
.my-area-name span{color:#bcd9f5}
.client-login{position:absolute;left:203px;top:22px;font-size:12.5px;color:#e1eefa}
.demo-link{position:absolute;left:361px;top:20px;font-family:"Source Sans 3",sans-serif;font-size:17.5px;color:#b7d4f0}
.contact-tab{position:absolute;top:7px;height:54px;background:#0d4f97;transform:skewX(-2deg);
  font-family:"Source Sans 3",sans-serif;font-size:22px;color:#fff;display:flex;align-items:center;justify-content:center}
.contact-tab.phone{left:588px;width:226px}
.contact-tab.email{left:826px;width:226px}

.legal{position:absolute;left:90px;top:1010px;font-size:12px;line-height:18px;color:#777}
</style>
</head>
<body>

<header>
  <div class="brand">
    <div class="brand-name">VelmaroneHealth</div>
    <div class="brand-tagline">Bringing Technology to Healthcare</div>
  </div>
  <nav class="main-nav">
    <a href="#" class="is-current">Home</a>
    <a href="#">Products<span class="amp">&amp;</span>Services</a>
    <a href="#">About Velmarone</a>
    <a href="#">News<span class="amp">&amp;</span>Events</a>
    <a href="#">Support</a>
    <a href="#">Contact</a>
  </nav>
</header>

<section class="hero">
  <h1 class="hero-title">Professional software solutions</h1>
  <p class="hero-lead">We develop software for the healthcare industry,<br>used daily by medical professionals</p>
  <div class="hero-photo" role="img" aria-label="Photograph of a smiling doctor and two nurses in blue scrubs"></div>
</section>

<aside class="sidebar">
  <h2 class="sidebar-title">Velmarone Blog</h2>
  <article class="post" style="top:86px">
    <h3 class="post-title">ALDERA Update</h3>
    <p class="post-text">Donec vitae elit nunc, id dictum velit. Phasellus diam arcu, imperdiet ut tristique eu, imperdiet at eros.</p>
    <a class="post-more" href="#">Read more</a>
  </article>
  <article class="post" style="top:201px">
    <h3 class="post-title">Pressure Ulcer Management System</h3>
    <p class="post-text">Nam venenatis aliquam eleifend. Aliquam aliq uam, nisi eget dapibus placerat, purus tellus tempor leo, sed vestibulum neque mauris non nisl.</p>
    <a class="post-more" href="#">Read more</a>
  </article>
  <article class="post" style="top:330px">
    <h3 class="post-title">Electronic Patient Record v2.0 released</h3>
    <p class="post-text">Nam venenatis aliquam eleifend. Aliquam aliq uam, nisi eget dapibus placerat, purus tellus tempor leo, sed vestibulum neque mauris non nisl.</p>
    <a class="post-more" href="#">Read more</a>
  </article>
</aside>

<main>
  <div class="showcase">
    <div class="showcase-boxes" role="img" aria-label="Product box illustrations for the Ward and Bed, Pressure Ulcer, Tissue Viability and other management systems"></div>
  </div>
  <h2 class="tagline">The <b>VelmaroneHealth</b> products family. All web-based.</h2>
  <p class="intro">Maecenas tempus sem ac neque. Fusce iaculis adipiscing laoreet. Etiam mattis mi et metus tincidunt non ornare ipsum commodo. Nulla in tortor justo.</p>
  <p class="body-copy">Sed lobortis, ligula sed ornare malesuada, lorem purus dapibus arcu, sit amet pulvinar arcu tellus vitae nunc. Nullam ac diam ut nisl pharetra consectetur non quis diam. Sed ipsum nisi, adipiscing vel pretium nec, fringilla vitae purus. Ut commodo tempor orci, eu consequat augue tempus duis.</p>
  <ul class="quick-links">
    <li><a href="#">Our Products and Services<svg width="6" height="10" viewBox="0 0 6 10"><path d="M1 1l4 4-4 4" fill="none" stroke="#555" stroke-width="1.2"/></svg></a></li>
    <li><a href="#">Request a Demonstration<svg width="6" height="10" viewBox="0 0 6 10"><path d="M1 1l4 4-4 4" fill="none" stroke="#555" stroke-width="1.2"/></svg></a></li>
    <li><a href="#">Contact Us<svg width="6" height="10" viewBox="0 0 6 10"><path d="M1 1l4 4-4 4" fill="none" stroke="#555" stroke-width="1.2"/></svg></a></li>
  </ul>
</main>

<div class="action-bar">
  <div class="my-area">
    <span class="my-area-name"><span>My </span>Velmarone</span>
    <a class="client-login" href="#">Client login <svg width="6" height="10" viewBox="0 0 6 10" style="margin-left:6px;vertical-align:-1px"><path d="M1 1l4 4-4 4" fill="none" stroke="#fff" stroke-width="1.2"/></svg></a>
  </div>
  <a class="demo-link" href="#">REQUEST A DEMONSTRATION</a>
  <div class="contact-tab phone">+44 (0) 208 555 0172</div>
  <div class="contact-tab email">info@velmarone.com</div>
</div>

<footer class="legal">
  <p>Copyright 2010, Velmarone Ltd.</p>
  <a href="#">Terms of Use</a>
</footer>

</body>
</html>
```